Lantern Marketing Group (LMG)

This is for my business cards. I want a Nice anfd Elegant Business Card to be Designed, Using more or less of the same colors of my logo that i have attached.i would like to have these business cards forever

Thank you

Thank you

Thank you

Contact Information for Business Card

Tobias Rennard
Lantern Marketing Group
C.(555) 214-6083
E-Mail. TRennard@lanternmgroup.example

Font styles to use
Serif
Sans Serif

Colors
d0dfed
cbcbcb
cee9f5

Requirements
Must have
• (LMG)
• Lantern Marketing Group
Nice to have
• 3D affects
Should not have
• Please try not using the flat version of the logo try and use the 3d version please

```html
<!DOCTYPE html>
<html lang="en">
<head>
<meta charset="utf-8">
<title>Lantern Marketing Group – Business Cards</title>
<link rel="stylesheet" href="https://fonts.googleapis.com/css2?family=Michroma&family=Roboto:wght@400&display=swap">
<style>
  :root {
    --bg: #e4e5e7;
    --brand-blue: #0b6cc6;
    --ice: #d6f4fa;
    --ice-light: #eafcff;
    --paper: #ffffff;
    --grey: #9b9b9b;
    --divider: #cbcbcb;
  }
  * { box-sizing: border-box; margin: 0; padding: 0; }
  html, body { width: 1200px; height: 800px; overflow: hidden; }
  body {
    background: var(--bg);
    font-family: "Roboto", Arial, sans-serif;
    position: relative;
  }
  .card {
    position: absolute;
    top: 252px;
    width: 520px;
    height: 297px;
    border-radius: 3px;
    box-shadow: 0 10px 24px rgba(0,0,0,0.12);
    overflow: hidden;
  }
  .card--front {
    left: 50px;
    background: linear-gradient(160deg, var(--ice) 0%, var(--ice-light) 100%);
    display: flex;
    align-items: center;
    justify-content: center;
  }
  .card--back {
    left: 630px;
    background: var(--paper);
  }
  .brand {
    display: flex;
    align-items: center;
    gap: 14px;
    color: var(--brand-blue);
    font-family: "Michroma", Arial, sans-serif;
  }
  .brand__square {
    width: 54px;
    height: 54px;
    background: var(--brand-blue);
    flex: none;
  }
  .brand__name {
    font-size: 22px;
    line-height: 1.25;
    letter-spacing: 1px;
    text-transform: uppercase;
  }
  .card--front .brand__name { font-size: 26px; }
  .card--front .brand__square { width: 66px; height: 66px; }

  .back__top {
    position: absolute;
    inset: 0 0 auto 0;
    height: 150px;
    background: linear-gradient(160deg, var(--ice) 0%, var(--ice-light) 100%);
    border-bottom: 3px solid var(--divider);
  }
  .holder {
    position: absolute;
    left: 28px;
    top: 26px;
  }
  .holder__name {
    font-family: "Michroma", Arial, sans-serif;
    font-size: 24px;
    color: var(--brand-blue);
    text-transform: uppercase;
    letter-spacing: 1px;
  }
  .holder__company {
    margin-top: 6px;
    font-size: 17px;
    color: var(--brand-blue);
  }
  .contact {
    position: absolute;
    right: 24px;
    top: 92px;
    list-style: none;
    color: var(--brand-blue);
    font-size: 14px;
  }
  .contact__item {
    display: flex;
    align-items: center;
    gap: 8px;
    margin-bottom: 8px;
  }
  .contact__icon { width: 20px; height: 20px; flex: none; }
  .card--back .brand {
    position: absolute;
    right: 26px;
    bottom: 30px;
  }
</style>
</head>
<body>
  <section class="card card--front" aria-label="Card front">
    <div class="brand">
      <span class="brand__square" aria-hidden="true"></span>
      <span class="brand__name">Lantern<br>Marketing Group</span>
    </div>
  </section>

  <section class="card card--back" aria-label="Card back">
    <div class="back__top"></div>
    <div class="holder">
      <h1 class="holder__name">Tobias Rennard</h1>
      <p class="holder__company">Lantern Marketing Group C.</p>
    </div>
    <ul class="contact">
      <li class="contact__item">
        <svg class="contact__icon" viewBox="0 0 20 20" aria-hidden="true">
          <circle cx="10" cy="10" r="9.5" fill="var(--brand-blue)"/>
          <path d="M7 5.5c.6-.4 1.2-.2 1.4.3l.7 1.6c.2.4 0 .9-.3 1.1l-.6.4c.5 1.2 1.4 2.1 2.6 2.6l.4-.6c.2-.3.7-.5 1.1-.3l1.6.7c.5.2.7.8.3 1.4-.6.9-1.6 1.3-2.6 1-2.6-.8-4.6-2.8-5.4-5.4-.3-1 .1-2 .8-2.8z" fill="#fff"/>
        </svg>
        <span>(555) 214-6083</span>
      </li>
      <li class="contact__item">
        <svg class="contact__icon" viewBox="0 0 20 20" aria-hidden="true">
          <circle cx="10" cy="10" r="9.5" fill="var(--brand-blue)"/>
          <rect x="5" y="6.5" width="10" height="7" fill="none" stroke="#fff" stroke-width="1.2"/>
          <path d="M5 6.5l5 4 5-4" fill="none" stroke="#fff" stroke-width="1.2"/>
        </svg>
        <span>TRennard@lanternmgroup.example</span>
      </li>
    </ul>
    <div class="brand">
      <span class="brand__square" aria-hidden="true"></span>
      <span class="brand__name">Lantern<br>Marketing Group</span>
    </div>
  </section>
</body>
</html>
```